Perfume Oil manufacturing and distribution company needs an emotion inspiring Wordpress Design

Must be Wordpress Design
Beautiful website needed for a company that manufactures and distributes scents that fragrance products from fine fragrances to personal care and household products. Please refer to attached file (namely "brief" for detailed explanation of our company, product and design requirements)

Website must be beautiful, and not too cluttered.

Must be coded for use in WordPress after design phase

remember not to flood website with pictures of perfumes and perfume bottles, this website is meant to inspire emotion...looking at the big fragrance brands (Valtorne and Merostel) one will not see pictures of perfume bottles etc. The site is all about emotion and smell and the senses.
Keep this in mind when submitting designs.

The site must captivate and inspire emotion with beautiful visuals.

the website must be about how one feels when surrounded by a beautiful smell, how one feels confident wearing a good scent. how freshly baked break reminds you of your grandmas house, or how a scent can remind of a seductive encounter, or a memory of fun times with friends out on the town, or as simple as the smell of a good cup of coffee or a rose to inspire a new days happenings.

all this emotion and feeling must be tied into the fact that Aroma Forge makes these moments through great smells. Which we supply to manufacturers of these great end products. whether it is a fine fragrance, a lotion, a car fragrance or a home spray. We scent the world around us.

try not to look too much at our existing website as this is outdated and the company has changed much since then, refer to this and the attached brief

Target Market(s)

small to medium businesses who manufacture products that need to be fragranced. whether these products be prestigious fine fragrances, daily personal care products or home care products, we make the fragrances that make these products beautiful.

Industry/Entity Type

Perfume

Coding

Coded - Design and coding required

Number of Pages Required

5+ page

Font styles to use
Serif
Sans Serif

Colors

Designer to choose colors to be used in the design.

Requirements
Must have
• must have full page header that captivates audience and inspires emotion (through a video or powerful imagery)
• Smell is a powerful emotion trigger and since a computer screen can not produce smell we will need to engage emotion through beautiful imagery and or video and beautiful design on the website. (refer to attached "brief" for more details)
• Must be coded for use in WordPress ONLY after design phase
• site must work well and look great on mobile since most of our audience use mobile to access our site.
Should not have
• too many pictures of perfume packaging and actual products, looking at the big fragrance manufacturers (Valtorne, Merostel, KDW) one will not see pictures of perfume bottles and packaging. This is very important as the website is more to inspire emotion and give a sense of how fragrance and perfume makes one feel.
• The site must captivate and inspire emotion with beautiful visuals.

```html
<!DOCTYPE html>
<html lang="en">
<head>
<meta charset="utf-8">
<title>Aroma Forge – Master Perfumers</title>
<link rel="stylesheet" href="https://fonts.googleapis.com/css2?family=Jost:wght@500;600;700&family=Open+Sans:wght@400;600;700&display=swap">
<style>
:root{
  --ink:#2e2e30;
  --paper:#f4f4f4;
  --white:#ffffff;
  --blue:#3a91d4;
  --blue-deep:#2f7fc0;
  --text-dark:#333336;
  --card-line:#e1e1e1;
  --hero-a:#3f4a2a;
  --hero-b:#6f7f3c;
  --hero-c:#a86a34;
}
*{box-sizing:border-box;margin:0;padding:0}
html,body{width:1200px;height:2228px;overflow:hidden}
body{position:relative;background:var(--paper);font-family:"Open Sans",Arial,sans-serif;color:var(--text-dark)}

/* hero */
.hero{position:absolute;left:0;top:0;width:1200px;height:710px;
  background:radial-gradient(ellipse at 35% 30%,#8fa653 0%,transparent 45%),
             radial-gradient(ellipse at 38% 45%,var(--hero-c) 0%,transparent 25%),
             radial-gradient(ellipse at 60% 75%,#4a2a18 0%,transparent 40%),
             linear-gradient(160deg,var(--hero-a),var(--hero-b) 50%,#2f3b22);}
.brand{position:absolute;left:112px;top:38px;display:flex;align-items:center;gap:12px;color:var(--white)}
.brand-dot{width:52px;height:52px;border-radius:50%;background:var(--white)}
.brand-name{font-family:"Jost",sans-serif;font-weight:600;font-size:34px;line-height:1}
.util-nav{position:absolute;right:112px;top:19px;display:flex;gap:24px;font-family:"Jost",sans-serif;font-size:13px;color:var(--white)}
.main-nav{position:absolute;right:100px;top:60px;display:flex;font-family:"Jost",sans-serif;font-weight:600;font-size:16px;color:var(--white)}
.main-nav span{padding:0 18px;border-left:1px solid rgba(255,255,255,.8);line-height:28px}
.main-nav span:last-child{border-right:1px solid rgba(255,255,255,.8)}
.play{position:absolute;left:551px;top:359px}

.curve{position:absolute;left:0;width:1200px}

/* values */
.values{position:absolute;left:0;top:686px;width:1200px;height:594px;background:var(--ink);color:var(--white)}
.section-title{font-family:"Jost",sans-serif;font-weight:700;font-size:38px;text-align:center;letter-spacing:.5px}
.values .section-title{position:absolute;top:106px;width:100%}
.value{position:absolute;left:118px;width:950px;font-size:16.5px;line-height:31px}
.value svg{position:absolute;left:0;top:0}
.value p{margin-left:45px}
.value b{font-weight:700}
.btn-about{position:absolute;left:511px;top:439px;width:178px;height:54px;border-radius:27px;background:var(--blue);
  display:flex;align-items:center;justify-content:center;gap:8px;font-family:"Jost",sans-serif;font-weight:700;font-size:21px;color:var(--white)}

/* products */
.products .section-title{position:absolute;top:1338px;width:100%;color:var(--text-dark)}
.card{position:absolute;top:1448px;width:226px;height:322px;background:var(--white);border:1px solid var(--card-line);text-align:center}
.card-img{position:absolute;left:50%;transform:translateX(-50%);bottom:130px;border-radius:8px;background:linear-gradient(90deg,#d9d6cf,#fbfaf7 45%,#cfcac1)}
.card h3{position:absolute;top:210px;width:100%;font-family:"Open Sans",sans-serif;font-weight:700;font-size:18.5px;color:var(--blue)}
.card .btn-view{position:absolute;left:47px;top:259px;width:131px;height:38px;border:2px solid var(--blue-deep);border-radius:19px;
  font-size:14px;font-weight:600;line-height:34px;color:var(--blue-deep)}

/* footer */
.footer{position:absolute;left:0;top:1860px;width:1200px;height:368px;
  background:radial-gradient(ellipse at 12% 80%,#5aa6e0 0%,transparent 30%),
             radial-gradient(ellipse at 80% 25%,#2f6fa6 0%,transparent 35%),
             var(--blue);}
.contact-title{position:absolute;left:111px;top:118px;font-family:"Jost",sans-serif;font-weight:700;font-size:25px;color:var(--white)}
.contact-mail{position:absolute;left:111px;top:166px;display:flex;align-items:center;gap:14px;font-size:26px;color:var(--white)}
.btn-call{position:absolute;left:572px;top:146px;width:279px;height:62px;border-radius:31px;background:var(--white);
  display:flex;align-items:center;justify-content:center;gap:12px;font-family:"Open Sans",sans-serif;font-weight:700;font-size:22px;color:var(--blue)}
.social-tab{position:absolute;left:1028px;top:88px;width:61px;height:168px;background:#2c3f8a;color:var(--white);
  font-family:"Open Sans",sans-serif;font-weight:700;font-size:24px;writing-mode:vertical-rl;display:flex;align-items:center;justify-content:center}
.social-dot{position:absolute;left:1012px;top:161px;width:32px;height:32px;border-radius:50%;background:#3f7ee8}
.footer-rule{position:absolute;left:111px;right:111px;top:295px;border-top:1px solid rgba(255,255,255,.25)}
.copyright{position:absolute;top:318px;width:100%;text-align:center;font-size:13px;color:var(--white)}
.build-code{position:absolute;right:28px;top:318px;font-size:13px;color:var(--white)}
</style>
</head>
<body>

<header class="hero" role="img" aria-label="Close-up photo of a glass dropper releasing perfume oil into an amber bottle among flowers and greenery">
  <div class="brand"><span class="brand-dot"></span><span class="brand-name">Aroma Forge</span></div>
  <nav class="util-nav"><span>ONLINE TRAINING</span><span>CAREERS</span><span>CONTACT US</span><span>&#9906;</span></nav>
  <nav class="main-nav"><span>HOME</span><span>AROMA FORGE</span><span>OUR SERVICES</span><span>OUR PRODUCTS</span><span>BLOG</span></nav>
  <svg class="play" width="98" height="98" viewBox="0 0 98 98" aria-label="Play video">
    <circle cx="49" cy="49" r="46" fill="none" stroke="#fff" stroke-width="4"/>
    <path d="M38 29 L68 49 L38 69 Z" fill="none" stroke="#fff" stroke-width="4" stroke-linejoin="round"/>
  </svg>
</header>

<section class="values">
  <svg class="curve" style="top:-26px" height="27" viewBox="0 0 1200 27" preserveAspectRatio="none"><path d="M0 0 Q600 30 1200 0 L1200 27 L0 27Z" fill="#2e2e30" transform="scale(1,-1) translate(0,-27)"/></svg>
  <h2 class="section-title">AROMA FORGE</h2>
  <div class="value" style="top:187px">
    <svg width="30" height="30" viewBox="0 0 30 30" fill="none" stroke="#fff" stroke-width="1.6"><path d="M4 26 L10 20 M8 26 L22 12 L18 8 L4 22 Z M22 12 L27 4 L18 8"/></svg>
    <p><b>Legitimacy</b> (over 80 years combined experience, industry affiliations with packaging, ethanol and chemicals give us the edge in truly understanding the industry in which we operate)</p>
  </div>
  <div class="value" style="top:273px">
    <svg width="32" height="32" viewBox="0 0 32 32" fill="none" stroke="#fff" stroke-width="1.6"><path d="M16 2 L21 8 H18 V14 H24 V11 L30 16 L24 21 V18 H18 V24 H21 L16 30 L11 24 H14 V18 H8 V21 L2 16 L8 11 V14 H14 V8 H11 Z"/></svg>
    <p><b>Servanthood</b> (we are here to serve each stakeholder: customers, suppliers, employees and shareholders)</p>
  </div>
  <div class="value" style="top:341px">
    <svg width="34" height="34" viewBox="0 0 34 34" fill="none" stroke="#fff" stroke-width="1.6"><path d="M17 7 a8 8 0 0 1 5 14 v4 h-10 v-4 a8 8 0 0 1 5 -14 Z M13 28 h8 M14 31 h6 M17 1 v3 M5 6 l2 2 M29 6 l-2 2 M1 16 h3 M30 16 h3"/></svg>
    <p><b>Execution</b> (99% done = ZERO% done, if it is not done until it is 100% done, we are pedantic about result orientated service)</p>
  </div>
  <div class="btn-about">ABOUT <svg width="18" height="18" viewBox="0 0 18 18"><circle cx="9" cy="9" r="9" fill="#fff"/><path d="M5 9 H12 M9 5.5 L12.5 9 L9 12.5" stroke="#3a91d4" stroke-width="2.2" fill="none"/></svg></div>
</section>

<section class="products">
  <h2 class="section-title">OUR PRODUCTS</h2>
  <article class="card" style="left:111px"><div class="card-img" role="img" aria-label="100g perfume oil bottle" style="width:40px;height:74px"></div><h3>100G PERFUME OIL</h3><span class="btn-view">VIEW MORE</span></article>
  <article class="card" style="left:361px"><div class="card-img" role="img" aria-label="200g perfume oil bottle" style="width:54px;height:108px"></div><h3>200G PERFUME OIL</h3><span class="btn-view">VIEW MORE</span></article>
  <article class="card" style="left:611px"><div class="card-img" role="img" aria-label="500g perfume oil bottle" style="width:58px;height:136px"></div><h3>500G PERFUME OIL</h3><span class="btn-view">VIEW MORE</span></article>
  <article class="card" style="left:862px"><div class="card-img" role="img" aria-label="1kg perfume oil bottle" style="width:50px;height:146px"></div><h3>1KG PERFUME OIL</h3><span class="btn-view">VIEW MORE</span></article>
</section>

<footer class="footer" role="img" aria-label="Blue-tinted photo of roses and small perfume bottles">
  <svg class="curve" style="top:-30px" height="31" viewBox="0 0 1200 31" preserveAspectRatio="none"><path d="M0 31 Q600 -28 1200 31 Z" fill="#3a91d4"/></svg>
  <h2 class="contact-title">CONTACT ME</h2>
  <div class="contact-mail"><svg width="26" height="20" viewBox="0 0 26 20"><rect width="26" height="20" rx="2" fill="#fff"/><path d="M1 2 L13 11 L25 2" stroke="#3a91d4" stroke-width="2" fill="none"/></svg>lena@aromaforge.co.za</div>
  <div class="btn-call"><svg width="30" height="30" viewBox="0 0 30 30" fill="none" stroke="#3a91d4" stroke-width="2"><path d="M8 3 L12 9 L9 12 Q12 18 18 21 L21 18 L27 22 L24 27 Q12 26 3 8 Z M17 3 a10 10 0 0 1 10 10 M17 8 a5 5 0 0 1 5 5"/></svg>CALL ME BACK</div>
  <div class="social-tab">Friendwall</div>
  <span class="social-dot"></span>
  <div class="footer-rule"></div>
  <p class="copyright">© 2018 Aroma Forge.&nbsp; All rights reserved.&nbsp; Term of Use</p>
  <span class="build-code">C16</span>
</footer>

</body>
</html>
```